A5 Flyer Aluminium & PVC Windows

A5 flyer design with one side Aluminium Windows and other side PVC Windows.
Must contain the following:
- The 8 reasons to choose a Varendo frame
* Frames from our own factory
* Top quality at low prices
* Always a suitable offer
* Sustainability is our top priority
* We offer you help with your subsidy application
* We have a showroom of over 250 m2 full of inspiration
* With more than 20 years of experience, we have everything available in facade technology
* Always a reference near you

see website: https://www.varendoraam.example/
On the PVC part it must be visible that the frame is PVC and on the aluminum side you should really be able to see that it is aluminum.

Photo is only a sample, feel free to use other photos.

Brochure will mostly be on the floor mat.

Target Market(s)

Private homeowners/familie who wants to renew their windows

Industry/Entity Type

Aluminium and PVC windows

Font styles to use
Sans Serif

Requirements
Must have
• Mention a 15-year warranty and "Scan the QR code and claim your discount"
Should not have
• No photos of people

```html
<!DOCTYPE html>
<html lang="en">
<head>
<meta charset="utf-8">
<title>Varendo Kozijn – Aluminium &amp; PVC Windows Flyer</title>
<link rel="stylesheet" href="https://fonts.googleapis.com/css2?family=Arimo:wght@700&family=Josefin+Sans:wght@400;600;700&display=swap">
<style>
  :root {
    --stage: #e9ebee;
    --blue-top: #58b4d6;
    --blue-mid: #2a7dbd;
    --blue-deep: #0a3576;
    --white: #ffffff;
    --ink-blue: #1b3f7d;
    --photo-light: #d9dde0;
    --photo-mid: #a9b0b6;
    --photo-dark: #6c747b;
  }
  * { box-sizing: border-box; margin: 0; padding: 0; }
  html, body {
    width: 1200px;
    height: 1200px;
    overflow: hidden;
    background: var(--stage);
  }
  .flyer {
    position: absolute;
    left: 210px;
    top: 50px;
    width: 780px;
    height: 1100px;
    overflow: hidden;
    background: linear-gradient(170deg, var(--blue-top) 0%, var(--blue-mid) 45%, var(--blue-deep) 100%);
    color: var(--white);
    font-family: "Josefin Sans", sans-serif;
  }
  .brand {
    position: absolute;
    left: 47px;
    top: 190px;
    display: flex;
    align-items: center;
    gap: 12px;
  }
  .brand-square {
    width: 22px;
    height: 22px;
    border: 2px solid var(--white);
  }
  .brand-name {
    font-weight: 700;
    font-size: 27px;
    line-height: 1;
  }
  .brand-tagline {
    position: absolute;
    left: 98px;
    top: 224px;
    font-size: 13px;
    font-weight: 700;
  }
  .photo {
    position: absolute;
    border: 4px solid var(--white);
  }
  .photo-window {
    left: 436px;
    top: 65px;
    width: 304px;
    height: 283px;
    border-radius: 6px 6px 6px 90px;
    background: linear-gradient(135deg, var(--photo-light) 0%, var(--photo-mid) 55%, var(--photo-dark) 100%);
  }
  .photo-workshop {
    left: 436px;
    top: 492px;
    width: 304px;
    height: 281px;
    border-radius: 90px 6px 6px 6px;
    background: linear-gradient(160deg, var(--photo-light) 0%, var(--photo-mid) 50%, var(--photo-dark) 100%);
  }
  .headline {
    position: absolute;
    left: 46px;
    top: 327px;
    font-family: "Arimo", sans-serif;
    font-weight: 700;
    font-size: 55px;
    line-height: 68px;
    letter-spacing: 0.5px;
    text-transform: uppercase;
  }
  .offer {
    position: absolute;
    left: 47px;
    top: 548px;
    width: 370px;
  }
  .offer-warranty {
    font-weight: 700;
    font-size: 20px;
    line-height: 24px;
    letter-spacing: 0.8px;
    text-transform: uppercase;
  }
  .offer-scan {
    font-weight: 600;
    font-size: 15px;
    line-height: 22px;
    margin-top: 4px;
  }
  .reasons-line {
    position: absolute;
    left: 36px;
    top: 618px;
  }
  .reasons {
    list-style: none;
    position: absolute;
    left: 81px;
    top: 622px;
  }
  .reasons li {
    height: 48px;
    font-size: 16.5px;
    line-height: 24px;
    letter-spacing: 0.5px;
    text-transform: uppercase;
  }
  .experience {
    position: absolute;
    left: 46px;
    top: 940px;
    font-size: 16.8px;
    line-height: 22px;
    font-weight: 600;
  }
  .web-rule {
    position: absolute;
    left: 300px;
    right: 0;
    top: 1050px;
    height: 3px;
    background: var(--white);
  }
  .web-pill {
    position: absolute;
    left: 47px;
    top: 1034px;
    width: 321px;
    height: 34px;
    border-radius: 17px;
    background: var(--white);
    color: var(--ink-blue);
    font-weight: 700;
    font-size: 17px;
    letter-spacing: 3px;
    display: flex;
    align-items: center;
    justify-content: center;
    padding-top: 3px;
  }
</style>
</head>
<body>
  <main class="flyer">
    <div class="brand">
      <span class="brand-square"></span>
      <span class="brand-name">Varendo Kozijn</span>
    </div>
    <p class="brand-tagline">Uw specialist</p>

    <div class="photo photo-window" role="img" aria-label="Photo of an opened white top-hung window frame in a grey wall"></div>

    <h1 class="headline">Aluminium<br>windows and<br>PVC windows</h1>

    <div class="offer">
      <p class="offer-warranty">15-year warranty</p>
      <p class="offer-scan">Scan the QR code and claim your discount</p>
    </div>

    <div class="photo photo-workshop" role="img" aria-label="Photo of a window frame being assembled on a workbench in the factory"></div>

    <svg class="reasons-line" width="46" height="312" viewBox="0 0 46 312" aria-hidden="true">
      <g fill="none" stroke="#ffffff" stroke-width="2" stroke-linecap="round" stroke-linejoin="round">
        <line x1="8" y1="6" x2="8" y2="304"/>
        <polyline points="3,298 8,306 13,298"/>
        <line x1="8" y1="14" x2="30" y2="14"/><polyline points="25,9 32,14 25,19"/>
        <line x1="8" y1="62" x2="30" y2="62"/><polyline points="25,57 32,62 25,67"/>
        <line x1="8" y1="110" x2="30" y2="110"/><polyline points="25,105 32,110 25,115"/>
        <line x1="8" y1="158" x2="30" y2="158"/><polyline points="25,153 32,158 25,163"/>
        <line x1="8" y1="206" x2="30" y2="206"/><polyline points="25,201 32,206 25,211"/>
        <line x1="8" y1="254" x2="30" y2="254"/><polyline points="25,249 32,254 25,259"/>
      </g>
    </svg>

    <ul class="reasons">
      <li>Frames from our own factory</li>
      <li>Top quality at low prices</li>
      <li>Always a suitable offer</li>
      <li>Sustainability is our top priority</li>
      <li>We offer you help with your subsidy application</li>
      <li>We have a showroom of over 250 m2 full of inspiration</li>
    </ul>

    <p class="experience">With more than 20 years of experience, we have everything available in facade technology<br>Always a reference near you</p>

    <div class="web-rule"></div>
    <div class="web-pill">www.varendoraam.example</div>
  </main>
</body>
</html>
```